C U B A N - C I G A R S - F L Y E R

I need a double-sided 5x7 club type flyer for a Memorial Day Weekend Trip.
The main side design needs to be similar to the attached flyer example. The front design of flyer is KEY. The design will be awarded to the closest finished submission to the example flyer.
Both sides of the flyer should also included event and business logo, which are also attached. Both logos can be altered to fit printing need accordingly.
Front side content is also attached.
The back side design will be very simple. Consists of 3 travel images and trip description, and my contact very details. Same color design as front. The attached word document contains backside details for REFERENCE ONLY. Please focus on front side when submitting a design for this project.
Target Market(s)
A F R I C A N - A M E R I C A N - C I G A R - S M O K E R S
Industry/Entity Type
Travel Industry
Requirements
Must have
- All the elements of the attached information
Nice to have
- Masculine Images
Should not have
- Large Cigar focus to catch customer's attention

```html
<!DOCTYPE html>
<html lang="en">
<head>
<meta charset="utf-8">
<title>Cuba Trip Memorial Day Weekend Flyer</title>
<link rel="stylesheet" href="https://fonts.googleapis.com/css2?family=Archivo:wght@700;800;900&family=Arimo:wght@400;700&family=Open+Sans:wght@400&display=swap">
<style>
  :root {
    --page: #8d8d8d;
    --ink-dark: #5a140c;
    --white: #ffffff;
    --paper-gold: #d9a04a;
    --paper-brown: #8a4a1c;
    --stamp-fill: #b8722e;
    --band: #c24f26;
    --band-dark: #a5381c;
    --text-brown: #3a1608;
  }
  * { box-sizing: border-box; margin: 0; padding: 0; }
  html, body { width: 1200px; height: 1200px; overflow: hidden; background: var(--page); }
  .canvas { position: relative; width: 1200px; height: 1200px; }
  .side { position: absolute; left: 237px; width: 726px; overflow: hidden; font-family: "Arimo", Arial, sans-serif; }
  .front { top: 56px; height: 517px; background: linear-gradient(120deg, #c98a3a, #d9a04a 40%, #a8521e 75%, #5a2a10); }
  .back { top: 618px; height: 518px; background: radial-gradient(ellipse at 55% 55%, #e2b060, #c98a3a 55%, #8a4a1c); }
  .abs { position: absolute; }
  .photo-bar { left: 0; top: 0; width: 268px; height: 517px; background: linear-gradient(180deg, #c0301c, #d8531e 45%, #a8281a 80%, #7a1e14); }
  .photo-still { left: 268px; top: 0; width: 458px; height: 517px; background: radial-gradient(ellipse at 70% 70%, #b8461c 0%, #c98a3a 45%, rgba(217,160,74,0.2) 80%), linear-gradient(180deg, #d6a050, #b87030); }
  .ring { border-radius: 50%; border: 2px solid var(--white); display: flex; align-items: center; justify-content: center; text-align: center; z-index: 2; }
  .ring.filled { background: var(--stamp-fill); }
  .brand-name { font-family: "Archivo", sans-serif; font-weight: 800; color: var(--white); font-size: 17px; line-height: 1.15; letter-spacing: 1px; }
  .stamp-name { font-family: "Archivo", sans-serif; font-weight: 800; color: var(--white); font-size: 24px; line-height: 1.05; }
  .c { text-align: center; }
  .pitch { left: 0; width: 268px; top: 206px; color: var(--white); font-weight: 700; font-size: 17px; line-height: 21px; }
  .pitch .big { font-family: "Archivo", sans-serif; font-weight: 900; font-size: 20px; }
  .rule { left: 33px; top: 342px; width: 224px; height: 2px; background: var(--white); }
  .weekend { left: 33px; color: var(--white); font-family: "Archivo", sans-serif; font-weight: 900; line-height: 1; }
  .headline { left: 282px; color: var(--ink-dark); font-family: "Archivo", sans-serif; font-weight: 800; white-space: nowrap; }
  .details { right: 14px; color: var(--white); font-weight: 700; font-size: 17px; text-align: right; white-space: nowrap; line-height: 22px; }
  .book { left: 582px; top: 457px; width: 129px; height: 42px; border: 2px solid var(--white); border-radius: 12px; color: var(--white); text-align: center; }
  .book b { display: block; font-size: 17px; margin-top: 3px; }
  .book span { display: block; font-size: 11px; font-weight: 700; }
  .photo-band { left: 76px; top: 26px; width: 562px; height: 228px; background: var(--band); opacity: .92; }
  .pic { top: 38px; height: 106px; border: 4px solid var(--white); z-index: 1; }
  .about { left: 98px; top: 153px; width: 512px; font-family: "Open Sans", sans-serif; font-size: 7.6px; line-height: 10.2px; color: var(--text-brown); text-align: justify; }
  .list { list-style: none; color: var(--text-brown); font-weight: 700; font-size: 11.5px; }
  .list li { position: relative; padding-left: 13px; }
  .list li::before { content: ""; position: absolute; left: 0; top: 5px; width: 5px; height: 5px; background: var(--text-brown); }
  .divider { left: 350px; top: 270px; width: 2px; height: 132px; background: var(--text-brown); }
  .footer-band { left: 0; top: 426px; width: 726px; height: 68px; background: linear-gradient(90deg, var(--band-dark), var(--band), var(--band-dark)); color: var(--white); padding: 10px 16px 0; }
  .footer-band b { display: block; font-size: 24px; line-height: 28px; }
  .footer-band span { display: block; font-size: 17px; line-height: 22px; }
</style>
</head>
<body>
<div class="canvas">

  <section class="side front">
    <div class="abs photo-still" role="img" aria-label="Photo of a glass of red wine, pine cones, autumn leaves and a cigar"></div>
    <div class="abs photo-bar" role="img" aria-label="Warm red-toned photo of a bar with bottles"></div>

    <div class="abs ring" style="left:61px;top:20px;width:156px;height:156px;">
      <span class="brand-name">SUNWARD<br>TRAVEL CO</span>
    </div>

    <div class="abs pitch c">
      Legally travel to Cuba<br>and return with real<br>
      <span class="big">CUBAN CIGARS!</span><br>
      TRIP NAME:<br>Rum Cigars and<br>Classic Cars
    </div>
    <div class="abs rule"></div>
    <div class="abs weekend" style="top:356px;font-size:26px;">MEMORIAL DAY</div>
    <div class="abs weekend" style="top:386px;font-size:39px;">WEEKEND</div>
    <div class="abs weekend" style="top:424px;font-size:66px;">2018!</div>

    <div class="abs headline" style="top:29px;font-size:21px;">A CUBA GIGAR GENTELEMEN'S</div>
    <div class="abs headline" style="top:52px;font-size:43px;font-weight:900;">MEMORIAL DAY</div>
    <div class="abs headline" style="top:101px;font-size:16px;font-weight:700;">CIGARS,RUM,&amp; CLASSIC CARS...........</div>

    <div class="abs ring" style="left:288px;top:156px;width:176px;height:176px;border-width:3px;">
      <span class="stamp-name">CUBA TRIP<br><span style="font-size:16px;">MAY 25-28</span></span>
    </div>

    <div class="abs details" style="top:384px;">DATES:FRIDAY,MAY 25TH - TUESDAY MAY 29TH</div>
    <div class="abs details" style="top:406px;">Book Today at www.sunwardtrips.com/cuba2018</div>
    <div class="abs details" style="top:428px;">For MoreInformational Call XXX-XXX-XXXX</div>
    <div class="abs book"><b>BOOK NOW</b><span>SPACE IS LIMITED</span></div>
  </section>

  <section class="side back">
    <div class="abs photo-band"></div>
    <div class="abs pic" style="left:98px;width:152px;background:linear-gradient(135deg,#d84a8a,#f0d030 45%,#2a7ad0);" role="img" aria-label="Photo of colourful classic American cars"></div>
    <div class="abs pic" style="left:264px;width:158px;background:linear-gradient(160deg,#eaf2fa,#b8d6ee);" role="img" aria-label="Map of the flight route from Miami to Havana, Cuba"></div>
    <div class="abs pic" style="left:434px;width:174px;background:linear-gradient(135deg,#6e3e22,#a8704a 50%,#5a3018);" role="img" aria-label="Close-up photo of Cuban cigars"></div>

    <div class="abs ring filled" style="left:13px;top:22px;width:118px;height:118px;border-width:3px;">
      <span class="stamp-name" style="font-size:17px;">CUBA TRIP<br><span style="font-size:12px;">MAY 25-28</span></span>
    </div>

    <p class="abs about">Cuba is the ultimate bucket list destination for any cigar lover. Now is your opportunity to legally travel to Cuba and experience a country that has been off limits to Americans for more than 50 years before it changes. Smoke fine Cuban cigars, meet its resilient people and experience Cuba's fascinating culture. Tour cigar factories, watch expert cigar rollers, visit a humidor factory and work shop, tour the Old Harbor Rum Museum to learn firsthand the process of making rum followed by rum tasting and pairings with Cuban cigars in a private setting and much more. Explore the Pinar Del Rio located in the Viñales Valley known for its stunning land scapes and tobacco plantations. Visit the world famous Vega Alta Tobacco Plantation to see first hand where and how the tobacco process is grown for fine Cuban Cigars. The bucket list trip of a lifetime awaits on this 'people to people' Cigar Journey to Cuba to learn first hand about Cuban cigars, meet the Cuban people, experience incredible cuisine, drive in classic American cars along the Malecon and experience the Cuban cigar process from <b><i>'seed to smoke'</i></b> and an opportunity to smoke in the birthplace of cigars!</p>

    <div class="abs ring" style="left:618px;top:154px;width:104px;height:104px;">
      <span class="brand-name" style="font-size:11px;">SUNWARD<br>TRAVEL CO</span>
    </div>

    <ul class="abs list" style="left:96px;top:277px;line-height:18.8px;">
      <li>Trip Cost: $2050</li>
      <li>Deposit: $300</li>
      <li>Payment plans available</li>
      <li>$300 Deposit Required</li>
      <li>Final payment Due By April 10, 2018</li>
      <li>*NON-REFUNDABLE</li>
      <li>*Passport Required</li>
    </ul>
    <div class="abs divider"></div>
    <div class="abs list" style="left:374px;top:264px;">What's Included:</div>
    <ul class="abs list" style="left:362px;top:279px;width:300px;line-height:14.4px;">
      <li>4 Days / 3 Nights</li>
      <li>5 Star Hotel Accommodations Based on Double Occupancy</li>
      <li>Roundtrip Palmway Airline Tickets from Fort Lauderdale Florida - Cuba</li>
      <li>Tour Bus Chauffeured Transportation</li>
      <li>All Rum and Cigar Tour Events</li>
      <li>Select Meals (Breakfast, Welcome and Farewell Dinner) and More!</li>
    </ul>

    <div class="abs footer-band">
      <b>$300 Deposit Required Final payment Due By April 10, 2018</b>
      <span>*NON-REFUNDABLE *Passport Required For More Information Call: XXX-XXX-XXXX</span>
    </div>
  </section>

</div>
</body>
</html>
```